Lani Wellness Clinic Website - this is a website for a medical practice

This is a medical practice and would like my logo to be presented. I have attached a copy of some copy that should give you an idea of what my practice is about. My practice will be seeing Elderaid patients in their homes. No coming to the office for a visit. I listen to my patients and provide individualized care. The name "Lani" means star in Hawaiʻian and want the patient to feel that they are the main focus of my practice.

Target Market(s)

Elderaid patients

Industry/Entity Type

medical

Coding

Coded - Design and coding required

Number of Pages Required

2 page

Font styles to use
Sans Serif

Colors
00AB8E
00BBA5
67D7C9
C6EFE9
E9F9F6

Requirements
Must have
• feeling that I care about each patient and that I will do my very best to keep them as healthy as possible, that the Hawaiʻian culture is represented. Simple and easy to navigate for someone who isnʻt tech savvy. In normal conversational language.
Nice to have
• The elderly in Hawaiʻi are called Kapuna and they are revered. I would like to convey that.
Should not have
• Medical jargon

```html
<!DOCTYPE html>
<html lang="en">
<head>
<meta charset="utf-8">
<title>Lani Wellness Clinic</title>
<link href="https://fonts.googleapis.com/css2?family=Poppins:wght@400;500;600;700&display=swap" rel="stylesheet">
<style>
:root{
  --teal:#00BBA5;
  --teal-dark:#00AB8E;
  --teal-mid:#67D7C9;
  --teal-pale:#C6EFE9;
  --teal-wash:#E9F9F6;
  --ink:#111;
  --text:#555;
  --black:#000;
  --white:#fff;
}
*{margin:0;padding:0;box-sizing:border-box}
html,body{width:1200px;height:5111px;overflow:hidden}
body{font-family:'Poppins',sans-serif;color:var(--ink);background:var(--white);position:relative}
.abs{position:absolute}
.btn{position:absolute;display:flex;align-items:center;justify-content:center;background:var(--teal);color:var(--white);font-size:13px;font-weight:600;text-transform:uppercase}
.btn.dark{background:var(--black)}
.rule{position:absolute;height:3px;width:60px;background:var(--teal)}
.section-title{position:absolute;left:0;width:1200px;text-align:center;font-size:50px;font-weight:600;line-height:1}
.photo{position:absolute}

/* top bar */
.topbar{top:0;left:0;width:1200px;height:36px;background:var(--teal);color:var(--white);font-size:14px}
.topbar span{position:absolute;top:8px;display:flex;align-items:center;gap:8px}
/* header */
.logo{left:86px;top:70px;font-size:28px;font-weight:500;color:var(--teal)}
.nav a{position:absolute;top:76px;font-size:12.5px;color:var(--ink);text-decoration:none}
.nav a.active{color:var(--teal)}
.nav a.active::after{content:"";position:absolute;left:-4px;right:-4px;top:28px;height:1px;background:var(--teal)}
.nav a.active::before{content:"";position:absolute;left:50%;top:25px;width:6px;height:6px;margin-left:-3px;border-radius:50%;background:var(--teal)}

/* hero */
.hero{top:138px;left:0;width:1200px;height:820px;background:linear-gradient(110deg,#4c4a3a 0%,#8a7356 35%,#c9a98a 55%,#6b5a44 80%,#3b3a2c 100%)}
.hero-arrow{position:absolute;width:40px;height:40px;border-radius:50%;top:403px;display:flex;align-items:center;justify-content:center}
.hero-panel{left:86px;top:518px;width:1027px;height:217px;background:rgba(30,30,30,.78)}
.hero-panel .kicker{position:absolute;left:83px;top:40px;font-size:18px;font-weight:500;color:var(--teal)}
.hero-panel h1{position:absolute;left:83px;top:68px;font-size:39px;font-weight:600;line-height:51px;color:var(--white)}

/* about */
.about-frame{left:123px;top:1047px;width:420px;height:466px;border:2px solid var(--teal)}
.about-title{left:654px;top:1098px;font-size:40px;font-weight:600}
.about-text{left:654px;top:1205px;width:424px;font-size:14.5px;line-height:31px;color:var(--text);text-align:justify}

/* services */
.card{position:absolute;background:var(--white);box-shadow:0 2px 14px rgba(0,0,0,.14)}
.svc-icon{position:absolute;left:29px;top:45px;width:91px;height:84px;background:var(--teal);display:flex;align-items:center;justify-content:center}
.svc-title{position:absolute;left:29px;top:152px;font-size:19px;font-weight:600}
.svc-text{position:absolute;left:29px;top:196px;width:266px;font-size:14px;line-height:25px;color:#777;text-align:justify}
.svc-link{position:absolute;left:32px;top:296px;font-size:13px;font-weight:600;color:var(--teal);text-decoration:underline}

/* stats */
.stats{top:2344px;left:0;width:1200px;height:345px;background:linear-gradient(90deg,var(--teal-dark),var(--teal) 50%,#2ccab5)}
.stat{position:absolute;width:260px;text-align:center;color:var(--white)}
.stat-box{width:116px;height:108px;margin:73px auto 0;border:3px solid var(--white);display:flex;align-items:center;justify-content:center}
.stat-box i{display:flex;width:98px;height:90px;background:var(--white);align-items:center;justify-content:center}
.stat b{display:block;margin-top:18px;font-size:38px;font-weight:600;line-height:1.1}
.stat span{display:block;margin-top:6px;font-size:20px}

/* testimonials */
.tcard{position:absolute;top:2935px;width:334px;height:254px;background:var(--white);border-radius:30px;box-shadow:0 3px 16px rgba(0,0,0,.13)}
.avatar{position:absolute;left:35px;top:-35px;width:70px;height:70px;border-radius:50%;background:linear-gradient(135deg,#d9c6b4,#8b7766)}
.quote{position:absolute;right:34px;top:18px;font-size:110px;line-height:1;color:#ececec;font-weight:700}
.ttext{position:absolute;left:40px;top:62px;width:254px;font-size:14px;line-height:23px;color:var(--text);text-align:justify}
.tline{position:absolute;left:40px;right:40px;top:178px;height:1px;background:#ddd}
.tname{position:absolute;left:40px;top:191px;font-size:12px;font-weight:600}
.trole{position:absolute;left:40px;top:208px;font-size:9.5px;color:#888}
.stars{position:absolute;right:46px;top:193px;font-size:11px;color:#f5b800;letter-spacing:1px}

/* home visit booking */
.appt{top:3367px;left:0;width:1200px;height:526px;background:linear-gradient(90deg,var(--teal-wash) 0%,var(--teal-pale) 45%,#8fd9cd 100%)}
.appt h2{position:absolute;left:89px;top:113px;font-size:40px;font-weight:600;line-height:48px}
.appt p{position:absolute;left:89px;top:258px;width:510px;font-size:14px;line-height:24px;color:#444}

/* blog */
.bcard{position:absolute;top:4105px;height:408px;background:var(--white);box-shadow:0 2px 14px rgba(0,0,0,.14)}
.bimg{position:absolute;left:6px;top:6px;right:6px;height:238px}
.bdate{position:absolute;left:20px;top:54px;height:28px;padding:0 14px;background:var(--white);font-size:10.5px;display:flex;align-items:center;gap:6px}
.btitle{position:absolute;left:24px;top:270px;width:280px;font-size:18.5px;font-weight:500;line-height:26px}
.btext{position:absolute;left:24px;top:330px;width:270px;font-size:14px;line-height:25px;color:#666}

/* footer */
.footer{top:4678px;left:0;width:1200px;height:371px;background:var(--black);color:var(--white)}
.fhead{position:absolute;top:83px;font-size:20px;font-weight:500}
.fhead::after{content:"";position:absolute;left:0;top:42px;width:48px;height:2px;background:var(--teal)}
.flinks div{position:absolute;left:185px;font-size:14.5px}
.flinks div::before{content:"›";position:absolute;left:-20px;top:-3px;color:var(--teal);font-size:18px}
.fcontact{position:absolute;left:426px;width:300px;font-size:14.5px;line-height:19px}
.fcontact i{position:absolute;left:0;top:0;width:30px;height:30px;border:1px solid #666;display:flex;align-items:center;justify-content:center}
.fcontact div{margin-left:52px}
.copybar{top:5049px;left:0;width:1200px;height:62px;background:var(--teal);color:var(--white);font-size:13px}
.social{position:absolute;top:15px;width:34px;height:34px;border:1.5px solid var(--white);display:flex;align-items:center;justify-content:center}
.social i{width:12px;height:12px;background:var(--white)}
</style>
</head>
<body>

<div class="abs topbar">
  <span style="left:86px">
    <svg width="16" height="16" viewBox="0 0 24 24" fill="none" stroke="#fff" stroke-width="2"><path d="M22 16.9v3a2 2 0 0 1-2.2 2 19.8 19.8 0 0 1-8.6-3.1 19.5 19.5 0 0 1-6-6A19.8 19.8 0 0 1 2.1 4.2 2 2 0 0 1 4.1 2h3a2 2 0 0 1 2 1.7c.1.9.4 1.8.7 2.7a2 2 0 0 1-.5 2.1L8 9.8a16 16 0 0 0 6 6l1.3-1.3a2 2 0 0 1 2.1-.4c.9.3 1.8.6 2.7.7a2 2 0 0 1 1.7 2z"/></svg>
    555-214-0387
  </span>
  <span style="right:76px">
    <svg width="20" height="14" viewBox="0 0 20 14" fill="none" stroke="#fff" stroke-width="1.6"><rect x="1" y="1" width="18" height="12"/><path d="M1 1l9 7 9-7"/></svg>
    hello@laniwellness.example
  </span>
</div>

<div class="abs logo">Lani Wellness Clinic</div>
<nav class="nav">
  <a class="active" style="left:463px">HOME</a>
  <a style="left:535px">ABOUT US</a>
  <a style="left:634px">SERVICES ▾</a>
  <a style="left:729px">TESTIMONIALS</a>
  <a style="left:853px">CONTACT US</a>
</nav>
<div class="btn" style="left:966px;top:64px;width:150px;height:36px;font-size:12px">Ask a Question</div>

<section class="abs hero" role="img" aria-label="Photo of a smiling kupuna and her caregiver sharing a warm moment outdoors">
  <div class="hero-arrow" style="left:45px;background:rgba(255,255,255,.75)">
    <svg width="10" height="10" viewBox="0 0 10 10"><path d="M7 1L3 5l4 4" stroke="#555" stroke-width="1.5" fill="none"/></svg>
  </div>
  <div class="hero-arrow" style="left:1114px;background:var(--teal)">
    <svg width="10" height="10" viewBox="0 0 10 10"><path d="M3 1l4 4-4 4" stroke="#fff" stroke-width="1.5" fill="none"/></svg>
  </div>
  <div class="abs hero-panel">
    <div class="kicker">ALOHA, WELCOME TO LANI WELLNESS CLINIC</div>
    <h1>Caring for our kūpuna,<br>right in your own home</h1>
    <div class="btn" style="left:749px;top:92px;width:196px;height:69px;font-size:18px;font-weight:500">Get Started</div>
  </div>
  <div class="abs" style="left:524px;top:742px;width:14px;height:14px;border-radius:50%;background:rgba(255,255,255,.7)"></div>
</section>

<div class="abs about-frame"></div>
<div class="photo" style="left:145px;top:1067px;width:420px;height:466px;background:linear-gradient(160deg,#e8e4dc,#a79a88 55%,#5e4f42)" role="img" aria-label="Photo of a caregiver pouring tea for a kupuna resting in bed at home"></div>
<h2 class="abs about-title">About Us</h2>
<div class="rule" style="left:654px;top:1154px"></div>
<p class="abs about-text">Lani means "star" in Hawaiʻian, and that is how we see you. Our kūpuna are treasured, so we bring care to your door. No trips to the office, no waiting rooms. We sit with you, listen to your story and make a plan that fits your life. Our promise is simple: to do our very best to keep you healthy and happy at home.</p>
<div class="btn" style="left:654px;top:1420px;width:187px;height:57px">Know More</div>

<h2 class="section-title" style="top:1650px">Our Services</h2>
<div class="rule" style="left:570px;top:1720px"></div>

<div class="card" style="left:86px;top:1791px;width:325px;height:355px">
  <div class="svc-icon"><svg width="56" height="48" viewBox="0 0 56 48" fill="none" stroke="#fff" stroke-width="2"><path d="M4 24L28 6l24 18"/><path d="M10 20v24h36V20"/><rect x="22" y="30" width="12" height="14"/><circle cx="40" cy="14" r="5"/></svg></div>
  <div class="svc-title">Care in Your Own Home</div>
  <div class="svc-text">We visit you where you feel most at ease. Check-ups, medicines and advice, all at home.</div>
  <div class="svc-link">READ MORE</div>
</div>
<div class="card" style="left:436px;top:1791px;width:326px;height:355px">
  <div class="svc-icon"><svg width="56" height="52" viewBox="0 0 56 52" fill="none" stroke="#fff" stroke-width="2"><circle cx="18" cy="8" r="5"/><circle cx="38" cy="8" r="5"/><path d="M18 14v18l-6 16M18 32l6 16M38 14v18l-6 16M38 32l6 16M18 20l20 0M44 20l6 28"/></svg></div>
  <div class="svc-title">Kūpuna Wellness Visits</div>
  <div class="svc-text">Regular visits to help you stay strong, steady and well, at your pace and in plain words.</div>
  <div class="svc-link">READ MORE</div>
</div>
<div class="card" style="left:787px;top:1791px;width:326px;height:355px">
  <div class="svc-icon"><svg width="56" height="52" viewBox="0 0 56 52" fill="none" stroke="#fff" stroke-width="2"><circle cx="20" cy="8" r="5"/><circle cx="36" cy="8" r="5"/><path d="M12 48V18h16v30M30 48V18h14v30M18 26h4M20 24v4"/></svg></div>
  <div class="svc-title">Care Made Just for You</div>
  <div class="svc-text">We listen first. Then we shape a care plan around you, your ʻohana and what matters most.</div>
  <div class="svc-link">READ MORE</div>
</div>
<div class="btn" style="left:520px;top:2203px;width:160px;height:52px">View More</div>

<section class="abs stats">
  <div class="stat" style="left:110px">
    <div class="stat-box"><i><svg width="52" height="44" viewBox="0 0 52 44" fill="none" stroke="#00BBA5" stroke-width="2.5"><circle cx="26" cy="10" r="7"/><path d="M4 30l12-6 10 6 10-6 12 6M10 40l16-8 16 8"/></svg></i></div>
    <b>25+</b><span>Years Of Caring</span>
  </div>
  <div class="stat" style="left:348px">
    <div class="stat-box"><i><svg width="40" height="48" viewBox="0 0 40 48" fill="#00BBA5"><circle cx="20" cy="12" r="9"/><path d="M4 46c0-12 7-20 16-20s16 8 16 20z"/><path d="M18 34h4v4h4v4h-4v4h-4v-4h-4v-4h4z" fill="#fff"/></svg></i></div>
    <b>750</b><span>Home Visits A Year</span>
  </div>
  <div class="stat" style="left:588px">
    <div class="stat-box"><i><svg width="56" height="44" viewBox="0 0 56 44" fill="#00BBA5"><circle cx="28" cy="12" r="8"/><circle cx="12" cy="16" r="6"/><circle cx="44" cy="16" r="6"/><path d="M14 42c0-10 6-18 14-18s14 8 14 18zM2 40c0-8 4-14 10-14 3 0 5 1 6 3-3 3-5 7-5 11zM54 40c0-8-4-14-10-14-3 0-5 1-6 3 3 3 5 7 5 11z"/></svg></i></div>
    <b>2K+</b><span>Happy ʻOhana</span>
  </div>
  <div class="stat" style="left:830px">
    <div class="stat-box"><i><svg width="44" height="48" viewBox="0 0 44 48" fill="#00BBA5"><path d="M10 2h24v14a12 12 0 0 1-24 0z"/><path d="M10 6H2v6a8 8 0 0 0 8 8M34 6h8v6a8 8 0 0 1-8 8" fill="none" stroke="#00BBA5" stroke-width="3"/><rect x="19" y="28" width="6" height="10"/><rect x="12" y="38" width="20" height="6"/></svg></i></div>
    <b>30+</b><span>Island Towns Served</span>
  </div>
</section>

<h2 class="section-title" style="top:2778px">Our Testimonials</h2>
<div class="rule" style="left:570px;top:2850px"></div>

<div class="tcard" style="left:75px">
  <div class="avatar" role="img" aria-label="Client portrait"></div>
  <div class="quote">❞</div>
  <p class="ttext">They come to Mom's house and really listen to her. She feels cared for, and we feel at peace. Mahalo nui loa to the whole team.</p>
  <div class="tline"></div>
  <div class="tname">Malia Kahale</div><div class="trole">Daughter of a patient</div>
  <div class="stars">★★★★★</div>
</div>
<div class="tcard" style="left:432px">
  <div class="avatar" role="img" aria-label="Client portrait"></div>
  <div class="quote">❞</div>
  <p class="ttext">No more long drives to the clinic. My visits happen at my kitchen table, and every question gets a kind, clear answer. So easy.</p>
  <div class="tline"></div>
  <div class="tname">Keoni Akana</div><div class="trole">Kupuna patient</div>
  <div class="stars">★★★★★</div>
</div>
<div class="tcard" style="left:789px">
  <div class="avatar" role="img" aria-label="Client portrait"></div>
  <div class="quote">❞</div>
  <p class="ttext">Tūtū is treated like family here. They take their time, speak in plain words and always treat our elders with real respect.</p>
  <div class="tline"></div>
  <div class="tname">Leilani Pua</div><div class="trole">Family caregiver</div>
  <div class="stars">★★★★★</div>
</div>
<div class="btn" style="left:520px;top:3236px;width:160px;height:52px">View More</div>

<section class="abs appt">
  <div class="photo" style="left:560px;top:0;width:640px;height:526px;background:linear-gradient(100deg,rgba(198,239,233,0) 0%,rgba(185,166,144,.55) 18%,#a58f78 40%,#8c7a66 65%,#cfc6bb 100%)" role="img" aria-label="Photo of a caregiver tending to a kupuna lying in bed at home"></div>
  <h2>Book A Home Visit<br>Today</h2>
  <div class="rule" style="left:89px;top:224px"></div>
  <p>Tell us a little about you or your loved one. We will call you back, answer your questions and come to your home at a time that suits you.</p>
  <div class="btn" style="left:89px;top:339px;width:161px;height:52px">Call Us Now</div>
  <div class="btn dark" style="left:262px;top:339px;width:222px;height:52px">Request A Visit</div>
</section>

<h2 class="section-title" style="top:3996px">Our Latest Blog</h2>
<div class="rule" style="left:570px;top:4065px"></div>

<div class="bcard" style="left:87px;width:320px">
  <div class="bimg" style="background:linear-gradient(150deg,#e7d6a2,#b89a73 50%,#5c4b40)" role="img" aria-label="Photo of a caregiver visiting an elderly man at home"></div>
  <div class="bdate"><svg width="10" height="10" viewBox="0 0 10 10" fill="none" stroke="#00BBA5"><rect x=".5" y="1.5" width="9" height="8"/><path d="M.5 4h9"/></svg>Feb 20, 2023</div>
  <div class="btitle">Simple ways to stay active and strong at home</div>
  <p class="btext">Easy daily habits that help kūpuna keep moving and feel well.</p>
</div>
<div class="bcard" style="left:438px;width:318px">
  <div class="bimg" style="background:linear-gradient(150deg,#7a2a22,#b0745a 50%,#3f2e2a)" role="img" aria-label="Photo of a caregiver holding a kupuna's hand"></div>
  <div class="bdate"><svg width="10" height="10" viewBox="0 0 10 10" fill="none" stroke="#00BBA5"><rect x=".5" y="1.5" width="9" height="8"/><path d="M.5 4h9"/></svg>Mar 12, 2023</div>
  <div class="btitle" style="text-decoration:underline">Honoring our kūpuna: care with aloha</div>
  <p class="btext">Why respect and listening are at the heart of every visit.</p>
</div>
<div class="bcard" style="left:795px;width:318px">
  <div class="bimg" style="background:linear-gradient(150deg,#cfd6dc,#8d8f92 50%,#3b3837)" role="img" aria-label="Photo of an elderly man resting with a caregiver beside him"></div>
  <div class="bdate"><svg width="10" height="10" viewBox="0 0 10 10" fill="none" stroke="#00BBA5"><rect x=".5" y="1.5" width="9" height="8"/><path d="M.5 4h9"/></svg>Apr 18, 2023</div>
  <div class="btitle">What to expect on your first home visit</div>
  <p class="btext">A friendly guide for you and your ʻohana, step by step.</p>
</div>
<div class="btn" style="left:520px;top:4555px;width:160px;height:52px">View More</div>

<footer class="abs footer">
  <div class="fhead" style="left:159px">Quick Links</div>
  <div class="fhead" style="left:426px">Contact Us</div>
  <div class="fhead" style="left:791px">Our Newsletter</div>

  <div class="flinks">
    <div style="top:164px">Home</div>
    <div style="top:195px">About Us</div>
    <div style="top:226px">Services</div>
    <div style="top:257px">Testimonials</div>
    <div style="top:288px">Contact Us</div>
  </div>

  <div class="fcontact" style="top:167px">
    <i><svg width="12" height="12" viewBox="0 0 24 24" fill="#fff"><path d="M22 17v3a2 2 0 0 1-2 2C10 21 3 14 2 4a2 2 0 0 1 2-2h3l2 5-2 2a14 14 0 0 0 7 7l2-2 5 2z"/></svg></i>
    <div>CALL US<br>555 214 0388</div>
  </div>
  <div class="fcontact" style="top:222px">
    <i><svg width="12" height="10" viewBox="0 0 12 10" fill="#fff"><path d="M0 0h12v10H0z"/><path d="M0 0l6 5 6-5" stroke="#000" fill="none"/></svg></i>
    <div>EMAIL US<br>hello@laniwellness.example</div>
  </div>
  <div class="fcontact" style="top:278px">
    <i><svg width="10" height="14" viewBox="0 0 10 14" fill="#fff"><path d="M5 0a5 5 0 0 1 5 5c0 4-5 9-5 9S0 9 0 5a5 5 0 0 1 5-5z"/><circle cx="5" cy="5" r="2" fill="#000"/></svg></i>
    <div>We come to you, at home<br>across the island</div>
  </div>

  <p class="abs" style="left:791px;top:166px;width:260px;font-size:14px;line-height:20px">Get health tips and clinic news by email.</p>
  <div class="abs" style="left:791px;top:224px;width:249px;height:38px;background:var(--white)"></div>
  <div class="btn" style="left:791px;top:275px;width:125px;height:34px;font-size:12px;font-weight:500">Subscribe</div>
</footer>

<div class="abs copybar">
  <span class="abs" style="left:86px;top:22px">Copyright © 2023 All Rights Reserved By Lani Wellness Clinic</span>
  <div class="social" style="left:960px"><i></i></div>
  <div class="social" style="left:1000px"><i></i></div>
  <div class="social" style="left:1040px"><i></i></div>
  <div class="social" style="left:1080px"><i></i></div>
</div>

</body>
</html>
```